vermalo web design

- Company / Site Description
We are developing a website that will allow anyone in Europe to find in one click, cultural things to do (Exhibition, Museum, Monument, Zoo, Aquarium, Archaeological site…) with friends or family, and to organize the visit (book a ticket / a private visit, book a restaurant nearby…).

Examples
1. You're in London with your girlfriend, it's saturday 10 am, you have two hours to spend and you want to see an exhibition. We provide you in one click all the exhibition matching your location / time and date.

2. You're in Berlin with some friends, it's thursday night you want to go out, but you don't know what to do. We provide you a list of experience, you can select for instance "I want to be on top of the world", and we show you a list of venues matching the selected experience / date / time /location of your request.

- Brand name : Vermalo
- Activity : Cultural Leisure, cultural entertainment

- Target audience
Broad target will be between 20 and 55. Core target will be between 25 and 40. Most likely to live in a city and in Europe.

- Behaviours and preferences
Our user is under time constraint (few minutes to find and choose his visit), idea constraint (is not sure about what to do and see) and money constraint.
He wants to have an easy to use website, not cluttered with information, focussed on added value information. He wants to have a website which is modern, fun and elegant that he will deem as professional and trustworthy.

- Our expectations (Do’s and Don’t)
We want to move away from traditional design. We want some OUT OF THE BOX design. Think of a website design that will look like an app design.
We want to make an awesome / extra ordinary /remember-able design. The design must be so cool, that the user wants to come back to the site. In two words: THINK EXTRAORDINARY.
You can use photos to help the user understand functions. If you use photo, use creative commons license photo.
Avoid black colors

- Functional Requirements
We need Four pages:
1. Home Page (desktop and mobile version): it’s both the homepage and the assistant page. This page will allow the user to find in one click his visit (please refer to the pdf file Assistant home page). The page must be self-explanatory for a first time user.
2. Assistant result page (desktop version): it’s the page that display the results found by the assistant based on the criteria search (please refer to the pdf file mockup - Assistant result page)
3. Site / Event page (desktop version): it’s the page that display each result information (please refer to the pdf file mockup – Event / Site Page)
The pdf files list all the elements include in each page + gives you a mockup of each page (just to put in perspective the element required). You are completely free about the design.
We don’t have the logo yet. Use a dummy logo for your page design.
The selected winner can expect to work with us immediately after the contest and on a on a regular basis later on.

- Technical Requirements
No Flash
For the winner, we will manage the CSS you will just need to provide :
. One PSD file containing all the pages
. Inside the PSD file we want for each page two groups: the first group will embed the desktop design, the second group will embed the responsive mobile design (Home Page only).
In total there should be 4 groups inside the PSD file (3 desktop groups, 1 mobile group).
Each group must contain all the elements specified in the pdf file

Website we like
http://demo.plandorix.example/?theme=Velunt
http://rosabel.quintorhub.example/#home
http://blogsite.fenk.daltoroute.example/2/
http://demo.plandorix.example/?theme=Mosaru
http://www.quarnivo.example/themes/lumbe/
http://gridmarket.example/item/tav-responsive-photography-blog-theme/full_screen_preview/8146027
http://items.zkvortel.example/?product=example
http://uk.harnoway.example

Reason: Due to the request of several designers, we have agreed to add 7 additional days to the contest deadline. Thank you. The vermalo team

Reason: We still need to collect all the votes. Sorry for the delay.

Reason: Hello, We extend the contest deadline, in order to collect all the votes from the poll. We should have everything finalized by sunday. Thank you vermalo team

```html
<!DOCTYPE html>
<html lang="en">
<head>
<meta charset="utf-8">
<title>Vermalo – Cultural things in Europe</title>
<link href="https://fonts.googleapis.com/css2?family=Open+Sans:ital,wght@0,400;0,600;0,700;1,400&family=Architects+Daughter&family=Kalam&display=swap" rel="stylesheet">
<style>
:root{
  --teal:#12928c;
  --orange:#ec8a12;
  --yellow:#f3d90a;
  --sky:#a9d3e6;
  --blue:#1c7fb6;
  --ink:#333;
  --dark:#2b2b2b;
  --mid:#555;
  --soft:#e6e6e6;
  --field:#e9e9e9;
  --white:#fff;
}
*{margin:0;padding:0;box-sizing:border-box}
html,body{width:1200px;height:2795px;overflow:hidden}
body{position:relative;font-family:"Open Sans",Arial,sans-serif;color:var(--ink);background:var(--soft)}
.abs{position:absolute}

/* hero */
.hero{left:0;top:0;width:1200px;height:742px;background:linear-gradient(100deg,#e8dcc4 0%,#d9c09a 35%,#c9a677 60%,#b49470 100%)}
.hero-photo{left:0;top:0;width:1200px;height:742px;background:radial-gradient(ellipse at 72% 45%,rgba(250,250,245,.55),rgba(0,0,0,0) 45%),linear-gradient(180deg,rgba(255,255,255,.25),rgba(0,0,0,.08))}
.topbar{top:0;height:28px;font-size:15px;font-weight:700;line-height:28px;text-align:center}
.tb-weather{left:436px;width:117px;background:#3b3b3b;color:#fff;font-weight:400}
.tb-assist{left:553px;width:140px;background:var(--teal);color:#fff}
.tb-fav{left:693px;width:151px;background:var(--sky);color:#0b4f6c}
.tb-arrow{left:844px;width:32px;background:var(--dark);color:#fff}
.tb-lang{left:876px;width:84px;background:var(--mid);color:#fff}
.tb-avatar{left:960px;width:33px;background:#7a6a5c}
.tb-login{left:993px;width:97px;background:#eee;color:#0b4f6c}
.logo-box{left:110px;top:0;width:194px;height:130px;background:rgba(255,255,255,.92);box-shadow:0 2px 6px rgba(0,0,0,.2);text-align:center}
.logo-dot{display:block;width:34px;height:34px;border-radius:50%;background:var(--orange);margin:24px auto 8px}
.logo-name{font-family:"Open Sans",serif;font-size:28px;color:var(--blue);font-weight:400}
.hero-title{left:114px;top:250px;font-size:76px;font-weight:700;color:var(--teal);letter-spacing:-1px}
.hero-sub{left:116px;top:336px;font-family:"Architects Daughter",cursive;font-size:36px;line-height:44px;color:#1c1c1c;text-transform:uppercase}
.hero-btn{left:110px;top:462px;width:313px;height:69px;background:var(--orange);color:#fff;font-size:26px;line-height:69px;padding-left:21px}
.hero-arrow{left:423px;top:462px;width:48px;height:69px;background:#fff}

/* sub nav */
.subnav{left:0;top:742px;width:1200px;height:82px;background:#fff}
.subnav-brand{left:138px;top:757px}
.subnav-brand b{display:block;color:var(--teal);font-size:19px}
.subnav-brand span{display:block;font-family:"Architects Daughter",cursive;font-size:12px;line-height:14px;color:#111;text-transform:uppercase}
.subnav-item{top:760px;width:196px}
.subnav-item i{display:block;font-family:"Kalam",cursive;font-style:normal;font-size:17px;color:#555}
.subnav-item b{display:block;font-size:15px;letter-spacing:.5px;color:#222}
.subnav-item b::after{content:"›";margin-left:22px}
.bar{top:816px;height:8px}
.crumbs{left:140px;top:838px;font-size:14px;color:#333}
.crumbs u{margin-right:10px}
.crumbs span{margin:0 10px}

/* intro */
.intro-title{left:0;top:922px;width:1200px;text-align:center;font-size:41px;line-height:50px;color:#444;letter-spacing:-1px}
.intro-title b{color:var(--teal);font-weight:600}
.intro-text{left:224px;top:1050px;width:752px;text-align:center;font-size:12.5px;line-height:19.5px;color:#444}

/* assistant */
.assistant{left:145px;top:1239px;width:906px;height:348px;background:#fff;border-top:5px solid var(--yellow)}
.map{left:390px;top:1322px;width:540px;height:240px;background:radial-gradient(ellipse,rgba(225,225,225,.9),rgba(255,255,255,0) 70%)}
.as-label{left:177px;top:1253px;font-size:18px;color:#444}
.tab{top:1246px;height:39px;line-height:39px;text-align:center;font-size:15px;color:#fff;background:var(--dark);clip-path:polygon(0 0,100% 0,94% 100%,6% 100%)}
.tab.on{background:var(--yellow);color:#333}
.badge{left:648px;top:1280px;width:64px;height:17px;border-radius:9px;background:var(--teal);color:#fff;font-size:10px;font-weight:700;text-align:center;line-height:17px}
.rule{left:145px;top:1313px;width:906px;height:1px;background:#e6e6e6}
.as-title{left:177px;top:1332px;font-size:23px;color:#222}
.radios{top:1387px;font-size:14px;color:#333}
.radio::before{content:"";display:inline-block;width:11px;height:11px;border:2px solid var(--teal);border-radius:50%;margin-right:5px;vertical-align:-1px}
.field-label{top:1442px;font-size:19px;color:#333}
.field{top:1474px;height:39px;background:var(--field);border:1px solid #ddd;font-size:13px;color:#888;line-height:37px;padding-left:10px}
.date-label{left:177px;top:1502px;font-size:18px}
.go-btn{left:177px;top:1526px;width:186px;height:37px;background:var(--orange);color:#fff;font-size:17px;font-weight:600;text-align:center;line-height:37px}
.down{left:559px;top:1614px;width:80px;height:68px;background:#fff}
.close{width:91px;height:28px}
.close span{position:absolute;left:0;top:0;width:63px;height:28px;background:var(--yellow);font-size:12px;font-weight:700;text-align:center;line-height:28px}
.close i{position:absolute;left:63px;top:0;width:28px;height:28px;background:#444}

/* want */
.want{left:0;top:1682px;width:1200px;height:772px;background:linear-gradient(180deg,#fff 0%,#e9e9e9 100%)}
.want-title{left:0;top:1760px;width:1200px;text-align:center;font-size:42px;color:var(--teal);font-weight:600}
.want-sub{left:0;top:1815px;width:1200px;text-align:center;font-size:16px;color:#333}
.tile{border-top:7px solid var(--yellow);overflow:hidden}
.tile .cap{position:absolute;left:0;bottom:0;width:100%;height:30px;background:rgba(0,0,0,.55);color:var(--yellow);font-size:16px;font-weight:700;line-height:30px;padding-left:10px}
.tile .plus{position:absolute;right:0;bottom:0;width:30px;height:30px;background:var(--yellow);color:#222;font-size:24px;line-height:28px;text-align:center}
.travel-list{left:145px;top:2245px;width:289px;height:78px;background:#fff;padding:10px 0 0 26px;font-size:12px;line-height:20px;color:#333;list-style:none}
.travel-list li::before{content:"•";color:var(--orange);margin:0 6px 0 -10px}
.cta{top:2383px;height:56px;line-height:56px;text-align:center;color:#fff;font-size:22px;box-shadow:0 4px 4px rgba(0,0,0,.25)}

/* footer */
.footer{left:0;top:2454px;width:1200px;height:294px;background:#fff}
.foot-mark{left:140px;top:2560px;font-size:24px;color:#999}
.foot-mark::before{content:"";display:inline-block;width:16px;height:16px;border-radius:50%;background:#bbb;margin-right:8px}
.foot-h{top:2512px;font-size:15px;font-weight:700;color:var(--teal)}
.foot-text{left:326px;top:2545px;width:176px;font-size:12.5px;line-height:17.6px;color:#333}
.follow{left:522px;top:2454px;width:186px;height:294px;background:#fff;box-shadow:0 0 14px rgba(0,0,0,.12)}
.social{left:557px;height:41px;font-size:13px;font-weight:700;color:var(--blue);line-height:41px}
.social i{display:inline-block;width:41px;height:41px;border-radius:50%;background:#222;vertical-align:top;margin-right:12px}
.video{left:773px;top:2553px;width:278px;height:158px;background:linear-gradient(135deg,#7a3c1c,#c2712c 45%,#3b5a7a);border:3px solid #eee}
.bottom{left:0;top:2748px;width:1200px;height:47px;background:#1c1c1c;color:#aaa;font-size:12px;line-height:47px}
</style>
</head>
<body>

<header>
  <div class="abs hero"></div>
  <div class="abs hero-photo" role="img" aria-label="Photo of a young couple reading a city map on a sunny beach"></div>

  <div class="abs topbar tb-weather">16°C</div>
  <div class="abs topbar tb-assist">MY ASSISTANT</div>
  <div class="abs topbar tb-fav">MY FAVOURITE</div>
  <div class="abs topbar tb-arrow">›</div>
  <div class="abs topbar tb-lang">ENGLISH</div>
  <div class="abs topbar tb-avatar" role="img" aria-label="User avatar"></div>
  <div class="abs topbar tb-login">LOGIN ▾</div>

  <div class="abs logo-box"><span class="logo-dot"></span><span class="logo-name">Vermalo</span></div>

  <h1 class="abs hero-title">IN EUROPE</h1>
  <p class="abs hero-sub">To find in one click,<br>cultural things</p>
  <div class="abs hero-btn">Start your journey here</div>
  <div class="abs hero-arrow">
    <svg width="48" height="69" viewBox="0 0 48 69"><path d="M24 22v26M14 38l10 10 10-10" fill="none" stroke="#777" stroke-width="2"/></svg>
  </div>
</header>

<nav>
  <div class="abs subnav"></div>
  <div class="abs subnav-brand"><b>IN EUROPE</b><span>To find in one click,<br>cultural things</span></div>
  <div class="abs subnav-item" style="left:386px"><i>Find out about</i><b>EXHIBITION</b></div>
  <div class="abs subnav-item" style="left:583px"><i>Find out about</i><b>MUSEUM</b></div>
  <div class="abs subnav-item" style="left:779px"><i>Find out about</i><b>MONUMENT</b></div>
  <div class="abs subnav-item" style="left:975px"><i>Find out about</i><b>AQUARIUM</b></div>
  <div class="abs bar" style="left:0;width:1200px;background:#ccc"></div>
  <div class="abs bar" style="left:337px;width:194px;background:var(--yellow)"></div>
  <div class="abs bar" style="left:531px;width:198px;background:var(--sky)"></div>
  <div class="abs bar" style="left:729px;width:196px;background:var(--yellow)"></div>
  <div class="abs bar" style="left:925px;width:197px;background:var(--blue)"></div>
  <div class="abs crumbs"><u>MyAssistant</u> ≫ <span>MyFavourites</span> ≫ <span>iSearch</span></div>
</nav>

<main>
  <h2 class="abs intro-title"><b>Book a ticket</b> / a private visit,<br>book a restaurant nearby...</h2>
  <p class="abs intro-text">It is a long established fact that a reader will be distracted by the readable content of a page when looking at its layout. The point of using Lorem Ipsum is that it has a more-or-less normal distribution of letters, as opposed to using 'Content here, content here', making it look like readable English. Many desktop publishing packages and web page editors now use Lorem Ipsum as their default model text, and a search for 'lorem ipsum' will uncover many web sites still in their infancy.</p>

  <section>
    <div class="abs assistant"></div>
    <div class="abs map" role="img" aria-label="Faint world map in the background"></div>
    <div class="abs as-label">MY ASSISTANT ⌄</div>
    <div class="abs tab on" style="left:332px;width:108px">✈ Flights</div>
    <div class="abs tab" style="left:440px;width:134px">✕ Restaurant</div>
    <div class="abs tab" style="left:578px;width:205px">✈ Flight + Restaurant</div>
    <div class="abs tab" style="left:794px;width:115px">▣ Bus</div>
    <div class="abs tab" style="left:921px;width:115px">▣ Rail</div>
    <div class="abs badge">SAVE MORE</div>
    <div class="abs rule"></div>
    <div class="abs as-title">Book a ticket / a private visit,</div>
    <div class="abs radios" style="left:194px">One way</div>
    <div class="abs radios radio" style="left:266px">Round Trip</div>
    <div class="abs radios radio" style="left:367px">Multi City / Stop Over</div>
    <svg class="abs" style="left:177px;top:1452px" width="14" height="14"><circle cx="7" cy="7" r="5" fill="none" stroke="#12928c" stroke-width="2"/><circle cx="7" cy="7" r="2" fill="#12928c"/></svg>
    <div class="abs field-label" style="left:391px">Time</div>
    <div class="abs field-label" style="left:572px">Location</div>
    <div class="abs field-label" style="left:783px">Weather</div>
    <div class="abs field" style="left:177px;width:199px">28 / Feb / 2014</div>
    <svg class="abs" style="left:344px;top:1483px" width="26" height="22"><rect x="1" y="3" width="20" height="16" fill="none" stroke="#777" stroke-width="2"/><line x1="1" y1="8" x2="21" y2="8" stroke="#777" stroke-width="2"/><circle cx="20" cy="16" r="5" fill="#eee" stroke="#777" stroke-width="2"/></svg>
    <div class="abs field" style="left:391px;width:127px">02:00</div>
    <div class="abs field" style="left:518px;width:41px;background:#bbb;color:#fff;padding:0;text-align:center">AM</div>
    <div class="abs field" style="left:572px;width:198px">Paris</div>
    <div class="abs field" style="left:730px;width:40px;background:#bbb;padding:0;text-align:center;color:#fff">▼</div>
    <div class="abs field" style="left:783px;width:108px;background:#f4f4f4;color:#666;font-size:18px;padding-left:44px">16°C</div>
    <svg class="abs" style="left:790px;top:1482px" width="34" height="24"><circle cx="12" cy="10" r="7" fill="#f3c51a"/><ellipse cx="20" cy="16" rx="11" ry="6" fill="#ddd"/></svg>
    <div class="abs date-label">Date</div>
    <div class="abs go-btn">WHAT YOU WANT</div>
    <div class="abs down"><svg width="80" height="68"><path d="M40 20v26M29 36l11 11 11-11" fill="none" stroke="#777" stroke-width="2"/></svg></div>
    <div class="abs close" style="left:960px;top:1653px"><span>CLOSE</span><i><svg width="28" height="28"><path d="M9 9l10 10M19 9L9 19" stroke="#fff" stroke-width="2"/></svg></i></div>
  </section>

  <section>
    <div class="abs want"></div>
    <h2 class="abs want-title">I WANT</h2>
    <p class="abs want-sub">A unique approach to search for a perfect view</p>

    <div class="abs tile" style="left:145px;top:1863px;width:181px;height:179px;background:linear-gradient(180deg,#c99a3c,#5e3e1c)" role="img" aria-label="Dreamy sunset over a lone chapel"><div class="cap">DREAM</div><div class="plus">+</div></div>
    <div class="abs tile" style="left:332px;top:1863px;width:380px;height:179px;background:radial-gradient(circle at 50% 55%,#2f8fe0,#0d2f5a 30%,#1a1a1a 60%)" role="img" aria-label="Close-up of a vivid blue eye"><div class="cap">ART</div><div class="plus">+</div></div>
    <div class="abs tile" style="left:717px;top:1863px;width:181px;height:179px;background:radial-gradient(circle at 50% 45%,#5a5a5a,#0a0a0a 70%)" role="img" aria-label="Dancer leaping on a dark stage"><div class="cap">BREATHE</div><div class="plus">+</div></div>
    <div class="abs tile" style="left:904px;top:1863px;width:147px;height:179px;background:linear-gradient(135deg,#9bb96a,#c07a3a 60%,#6a4a2a)" role="img" aria-label="Two rabbits in the grass"><div class="cap">ANIMAL</div><div class="plus">+</div></div>

    <div class="abs tile" style="left:145px;top:2066px;width:289px;height:179px;background:linear-gradient(180deg,#3e5fa0,#e79a3a 55%,#3a2a20)" role="img" aria-label="Eiffel Tower at sunset"><div class="cap">TRAVEL</div><div class="plus">−</div></div>
    <div class="abs tile" style="left:440px;top:2066px;width:223px;height:179px;background:linear-gradient(135deg,#8fb06a,#caa48a 55%,#6a8a5a)" role="img" aria-label="Portrait of a celebrity outdoors"><div class="cap">CELEBRITIES</div><div class="plus">+</div></div>
    <div class="abs tile" style="left:669px;top:2066px;width:229px;height:179px;background:linear-gradient(180deg,#6a7fc0,#e9a05a 60%,#2a2a3a)" role="img" aria-label="Friends jumping on a beach at sunset"><div class="cap">HAVE FUN</div><div class="plus">+</div></div>
    <div class="abs tile" style="left:904px;top:2066px;width:147px;height:179px;background:radial-gradient(circle at 40% 50%,#555,#0c0c0c 70%)" role="img" aria-label="Magician performing on stage"><div class="cap">MAGICIAN</div><div class="plus">+</div></div>

    <ul class="abs travel-list"><li>Paris</li><li>Germany</li><li>Italy</li></ul>

    <div class="abs cta" style="left:442px;width:247px;background:var(--teal)">CLICK HERE TO GO</div>
    <div class="abs cta" style="left:695px;width:93px;background:#2a2a2a">PLUS</div>
    <div class="abs close" style="left:960px;top:2424px"><span>CLOSE</span><i><svg width="28" height="28"><path d="M9 9l10 10M19 9L9 19" stroke="#fff" stroke-width="2"/></svg></i></div>
  </section>
</main>

<footer>
  <div class="abs footer"></div>
  <div class="abs foot-mark">Vermalo</div>
  <h3 class="abs foot-h" style="left:326px">ABOUT US</h3>
  <p class="abs foot-text">It is a long established fact that a reader will be distracted by the readable content of a page when looking at its layout. The point of using Lorem Ipsum is that it has a more-or-less normal distribution of letters, as</p>
  <div class="abs follow"></div>
  <h3 class="abs foot-h" style="left:561px">FOLLOW US</h3>
  <div class="abs social" style="top:2549px"><i></i>Pagemix</div>
  <div class="abs social" style="top:2599px"><i></i>Chirpline</div>
  <div class="abs social" style="top:2659px"><i></i>Circlenet</div>
  <h3 class="abs foot-h" style="left:775px">OUR VIDEO</h3>
  <div class="abs video" role="img" aria-label="Video thumbnail of a colourful fantasy battle scene"></div>
  <div class="abs bottom"><span style="position:absolute;left:149px">Privacy Policy &nbsp;|&nbsp; Site Map</span><span style="position:absolute;right:149px">Copyright 2014- All rights reserved</span></div>
</footer>

</body>
</html>
```